Our Family Values Printed on Canvas for our Home

My family has decided on the following values:

Be Grateful
Act Kindly
Stay Honest
Smile Often
Do Your Best
Live Adventurously
Never Stop Learning
Help Others
Love Always

We desire to print a sign (on 16x20 or 20x16 canvas) for various rooms in our house to remind us of the family we want to be. Each value has equal value, and we want the sign to reflect that (for example, we don't want one value to appear larger than another). We are not particular about colors or images however here are some hints about us that may help:
- My wife's favorite color is dark teal
- We live in the Pacific Northwest
- We love nature
- My wife and I have two sons and a dog

We look forward to your design!

--Tobias

Target Market(s)

Our family and friends

Industry/Entity Type

Non-Profit

Font styles to use
Decorative

Requirements
Must have
• - Printable on 16x20 or 20x60 canvas
• - Equal emphasis on each value
• - Easy to read

```html
<!DOCTYPE html>
<html lang="en">
<head>
<meta charset="UTF-8">
<title>Family Values Canvas Set</title>
<link href="https://fonts.googleapis.com/css2?family=Montserrat:wght@600;700&display=swap" rel="stylesheet">
<style>
  :root {
    --page-bg: #ffffff;
    --teal: #265862;
    --ink: #ffffff;
    --emblem-tone: #e6eeef;
  }
  html, body {
    margin: 0;
    padding: 0;
    width: 1200px;
    height: 640px;
    overflow: hidden;
    background: var(--page-bg);
  }
  .canvas {
    position: relative;
    width: 1200px;
    height: 640px;
    background: var(--page-bg);
  }
  .value-card {
    position: absolute;
    top: 146px;
    width: 278px;
    height: 348px;
    background: var(--teal);
    color: var(--ink);
    font-family: "Montserrat", sans-serif;
    text-align: center;
  }
  .value-card--best { left: 133px; }
  .value-card--learning { left: 462px; }
  .value-card--smile { left: 792px; }

  .value-card__emblem {
    position: absolute;
    top: 68px;
    left: 50%;
    width: 91px;
    height: 80px;
    margin-left: -45.5px;
    border-radius: 6px 6px 40px 40px / 6px 6px 14px 14px;
    background: var(--emblem-tone);
  }
  .value-card__lead {
    position: absolute;
    top: 176px;
    left: 0;
    right: 0;
    margin: 0;
    font-size: 18px;
    font-weight: 600;
    letter-spacing: 0.3px;
    line-height: 24px;
  }
  .value-card__word {
    position: absolute;
    top: 200px;
    left: 0;
    right: 0;
    margin: 0;
    font-size: 44px;
    font-weight: 700;
    letter-spacing: 0;
    line-height: 56px;
  }
</style>
</head>
<body>
  <main class="canvas">
    <section class="value-card value-card--best">
      <div class="value-card__emblem" role="img" aria-label="Light emblem artwork above the value"></div>
      <p class="value-card__lead">DO YOUR</p>
      <p class="value-card__word">BEST</p>
    </section>
    <section class="value-card value-card--learning">
      <div class="value-card__emblem" role="img" aria-label="Light emblem artwork above the value"></div>
      <p class="value-card__lead">NEVER STOP</p>
      <p class="value-card__word">LEARNING</p>
    </section>
    <section class="value-card value-card--smile">
      <div class="value-card__emblem" role="img" aria-label="Light emblem artwork above the value"></div>
      <p class="value-card__lead">SMILE</p>
      <p class="value-card__word">OFTEN</p>
    </section>
  </main>
</body>
</html>
```